Vello Shawarma Restaurant packging desgin

I want a packging desgin for my new Shawarma restaurant. The desgin should be modern and simple. I have added the logo and the identity in the attachment in PSD format so you can use it in the desgin. I also added some packging idea you may use it as background of your desgin. The main colors to be used is Red, grey, black and white.
Updates

Project Deadline Extended
Reason: Still i did not find an attractive desgin. I will try to provied you with feedback for each post

Target Market(s)

Food industry

Industry/Entity Type

Fast Food Restaurant

Font styles to use
Sans Serif

Colors
ec1f27
000000
919191
ffffff
eeeeee

Requirements
Must have
• The logo and the name VELLO. All boxes should be in the same theme
Nice to have
• Creative desgin and Twitter and instagram logo on the side
Should not have
• real food pictures

```html
<!DOCTYPE html>
<html lang="en">
<head>
<meta charset="utf-8">
<title>Vello Shawarma – Box Dieline</title>
<link rel="stylesheet" href="https://fonts.googleapis.com/css2?family=Jost:wght@600&family=Open+Sans:wght@400&display=swap">
<style>
  :root {
    --brand-red: #ec1f27;
    --brand-grey: #919191;
    --brand-black: #000000;
    --brand-white: #ffffff;
    --canvas-bg: #cccccc;
  }
  * { margin: 0; padding: 0; box-sizing: border-box; }
  html, body { width: 1200px; height: 1200px; overflow: hidden; background: var(--canvas-bg); }
  .dieline { position: relative; width: 1200px; height: 1200px; }
  .panel { position: absolute; background: var(--brand-red); overflow: hidden; }
  .flap-top    { left: 251px; top: 199px; width: 693px; height: 169px; }
  .flap-bottom { left: 251px; top: 832px; width: 693px; height: 169px; }
  .face-main   { left: 251px; top: 389px; width: 693px; height: 423px; }
  .side-left   { left: 64px;  top: 389px; width: 169px; height: 423px; }
  .side-right  { left: 966px; top: 389px; width: 169px; height: 423px; }

  .stripe-art-main {
    position: absolute; left: 0; top: 0; width: 272px; height: 423px;
    border-bottom-right-radius: 100% 70%;
    background: linear-gradient(150deg, #ffffff 0%, #fbe3e4 55%, #f6b9bc 100%);
  }
  .stripe-art-side {
    position: absolute; bottom: 0; width: 150px; height: 121px;
    background: linear-gradient(170deg, #f6b9bc 0%, #ffffff 100%);
  }
  .side-left .stripe-art-side  { left: 10px; border-top-right-radius: 100% 100%; border-top-left-radius: 30% 40%; }
  .side-right .stripe-art-side { left: 0;  border-top-right-radius: 100% 100%; border-top-left-radius: 30% 40%; }

  .brand-lockup {
    position: absolute; left: 415px; top: 28px; height: 70px;
    display: flex; align-items: center; gap: 20px;
  }
  .brand-name {
    font-family: 'Jost', sans-serif; font-weight: 600; font-size: 50px;
    color: var(--brand-white); letter-spacing: 1px; line-height: 1;
  }
  .brand-dot { width: 70px; height: 70px; border-radius: 50%; background: var(--brand-white); }

  .ingredient-band { position: absolute; left: 0; top: 351px; width: 693px; height: 72px; }

  .social-dots {
    position: absolute; top: 17px; width: 14px;
    display: flex; flex-direction: column; gap: 6px;
  }
  .social-dots span { display: block; width: 14px; height: 14px; border-radius: 50%; background: var(--brand-black); }
  .side-left .social-dots { left: 9px; }
  .side-right .social-dots { left: 146px; }

  .social-handle {
    position: absolute; top: 82px; width: 16px; height: 100px;
    font-family: 'Open Sans', sans-serif; font-size: 11px; line-height: 16px;
    color: var(--brand-black); writing-mode: vertical-rl; white-space: nowrap;
  }
  .side-left .social-handle { left: 8px; }
  .side-right .social-handle { left: 145px; }
  .side-rule { position: absolute; top: 178px; width: 3px; height: 210px; background: var(--brand-black); }
  .side-left .side-rule { left: 14px; }
  .side-right .side-rule { left: 151px; }
</style>
</head>
<body>
<main class="dieline">
  <section class="panel flap-top"></section>

  <section class="panel side-left">
    <div class="stripe-art-side" role="img" aria-label="White curved shawarma stripe illustration"></div>
    <div class="social-dots"><span></span><span></span><span></span></div>
    <div class="social-handle">velloshawarma</div>
    <div class="side-rule"></div>
  </section>

  <section class="panel face-main">
    <div class="stripe-art-main" role="img" aria-label="Large white shawarma spit illustration in curved stripes"></div>
    <div class="brand-lockup">
      <span class="brand-name">VELLO</span>
      <span class="brand-dot"></span>
    </div>
    <svg class="ingredient-band" viewBox="0 0 693 72" role="img" aria-label="Grey band with ingredient icons: meat, chicken, wrap, onion, shawarma, lettuce, skewer, bread">
      <polygon points="119,0 693,0 693,72 54,72" fill="var(--brand-grey)"/>
      <g fill="none" stroke="var(--brand-white)" stroke-width="2">
        <circle cx="151" cy="36" r="28"/>
        <circle cx="221" cy="36" r="28"/>
        <circle cx="291" cy="36" r="28"/>
        <circle cx="361" cy="36" r="28"/>
        <circle cx="431" cy="36" r="28"/>
        <circle cx="501" cy="36" r="28"/>
        <circle cx="571" cy="36" r="28"/>
        <circle cx="641" cy="36" r="28"/>
      </g>
    </svg>
  </section>

  <section class="panel side-right">
    <div class="stripe-art-side" role="img" aria-label="White curved shawarma stripe illustration"></div>
    <div class="social-dots"><span></span><span></span><span></span></div>
    <div class="social-handle">velloshawarma</div>
    <div class="side-rule"></div>
  </section>

  <section class="panel flap-bottom"></section>
</main>
</body>
</html>
```